Website for a Psychologist in Private Practice

I need a cool web design for my website: www.drvalporte.com. I would like it to look professional. Keep all the current content and add: Space for video; radio spots (see Silver Harbor Tunes Logo below for those); Quick Inquiry; Chatterbook link; 5 star rating on Rivo; a map; reviews from former patients. I am open to suggestions.

Target Market(s)

Those seeking individual and marital counseling.

Industry/Entity Type

Mental Health

Number of Pages Required

1 page

Font styles to use
Sans Serif
Other font styles liked:
• I'm open but no hard to read script

Requirements
Must have
• All the content on my home page with link for video and radio spots. List services and degrees and expertices (pics not necessary).
Nice to have
• A video of me and radio conversations (logo of Silver Harbor Tunes radio attached).
Should not have
• Cartoons, comedy, etc.... I don't need pictures of services (marital, depression, etc...) Just list those.

```html
<!DOCTYPE html>
<html lang="en">
<head>
<meta charset="utf-8">
<title>Dr. Mara L. Valporte — Clinical Psychologist</title>
<link rel="stylesheet" href="https://fonts.googleapis.com/css2?family=Source+Sans+3:wght@400;600;700;900&display=swap">
<style>
:root{
  --blue:#1f6fd6;
  --blue-dark:#0d4fb0;
  --blue-light:#3d8ef0;
  --ink:#111;
  --rule:#cfcfcf;
  --panel:#e4e4e4;
  --footer:#1b1b1b;
  --footer-text:#bdbdbd;
  --leaf:#6fa23a;
  --leaf-dark:#1f3a12;
}
*{margin:0;padding:0;box-sizing:border-box}
html,body{width:1200px;height:2514px;overflow:hidden;background:#fff}
body{position:relative;font-family:"Source Sans 3",Arial,sans-serif;color:var(--ink)}
.abs{position:absolute}

/* header */
.site-header{left:0;top:0;width:1200px;height:84px;background:linear-gradient(180deg,var(--blue-light),var(--blue-dark));}
.brand{left:25px;top:10px;color:#fff;font-weight:700;line-height:1}
.brand-name{font-size:36px}
.brand-role{font-size:22px;margin-top:4px}
.main-nav{left:595px;top:0;height:84px;display:flex}
.main-nav a{width:121px;height:84px;display:flex;align-items:center;justify-content:center;color:#fff;font-weight:700;font-size:22px;text-decoration:none;border-left:2px solid rgba(255,255,255,.25)}

/* hero */
.hero{left:0;top:109px;width:1200px;height:538px;background:radial-gradient(ellipse at 75% 40%,#b9e04c 0%,#7fb236 30%,#3c6a1c 60%,var(--leaf-dark) 100%)}
.hero-shadow{left:90px;top:640px;width:1020px;height:40px;background:radial-gradient(ellipse at 50% 0%,rgba(0,0,0,.35),rgba(0,0,0,0) 70%)}
.hero-title{left:67px;top:258px;color:#fff;font-weight:900;font-size:60px;line-height:60px;text-shadow:0 2px 4px rgba(0,0,0,.4)}
.hero-sub{left:73px;top:450px;width:420px;color:#fff;font-weight:700;font-size:17px;line-height:20px;text-shadow:0 1px 3px rgba(0,0,0,.5)}
.slider-dots{left:536px;top:664px;display:flex;gap:8px}
.slider-dots span{width:26px;height:26px;border-radius:50%;background:#000}
.slider-dots span.active{background:var(--blue);border:3px solid #000}

/* content */
.rule{height:2px;background:var(--rule)}
.section-title{color:var(--blue);font-weight:900;font-size:35px;line-height:40px;text-shadow:0 2px 2px rgba(0,0,0,.25)}
.copy p{font-weight:600;font-size:16.5px;line-height:22.5px;margin-bottom:22px}
.side-title{width:372px;text-align:center;color:var(--blue-dark)}
.side-list{width:372px;text-align:center;font-weight:600;font-size:16.5px;line-height:20.5px}
.portrait{left:798px;top:766px;width:373px;height:411px;background:linear-gradient(160deg,#7a9a6a,#d8b890 50%,#3a6fa8)}

/* media panel */
.media-panel{left:28px;top:1668px;width:1145px;height:519px;background:linear-gradient(180deg,#efefef,var(--panel));border:1px solid #d2d2d2}
.media-card{top:1728px;width:334px;height:396px;background:#fff;box-shadow:0 3px 6px rgba(0,0,0,.35)}
.card-head{height:60px;background:linear-gradient(180deg,var(--blue-light),var(--blue-dark));color:#fff;font-weight:700;font-size:36px;text-align:center;line-height:60px}
.player{left:17px;top:75px;width:298px;height:262px}
.more{left:0;top:348px;width:334px;display:flex;justify-content:center;align-items:center;gap:14px;font-weight:700;font-size:18px}
.more span.btn{background:#000;color:#fff;border-radius:6px;padding:6px 26px}
.poster{left:17px;top:75px;width:300px;height:300px;background:linear-gradient(180deg,#e32b6b 0%,#c8c2b8 25%,#9c8070 70%,#d6246a 100%)}

/* footer */
.site-footer{left:0;top:2187px;width:1200px;height:327px;background:linear-gradient(180deg,#2b2b2b,#0e0e0e)}
.foot-title{color:#fff;font-weight:700;font-size:22px}
.foot-list{color:var(--footer-text);font-size:14.5px;line-height:30px}
.map{left:585px;top:2229px;width:189px;height:186px;background:linear-gradient(135deg,#e8e6e0,#d7e3cf)}
.donate{left:825px;top:2226px;width:294px;text-align:center;color:var(--footer-text);font-size:14px;font-weight:600}
.badge-a{left:825px;top:2258px;width:139px;height:45px;background:#9cae4a}
.badge-b{left:980px;top:2258px;width:139px;height:45px;background:#fff}
.badge-rating{left:835px;top:2348px;width:65px;height:65px;background:#fff;border:3px solid #c4122f}
.share{left:1026px;top:2380px;width:93px;height:34px;background:#4a6fb5;border-radius:4px;color:#fff;font-size:12px;font-weight:700;display:flex;align-items:center;justify-content:center}
.copyright{left:0;top:2475px;width:1200px;text-align:center;color:var(--footer-text);font-size:14px;font-weight:700}
</style>
</head>
<body>

<header class="site-header abs">
  <div class="brand abs"><div class="brand-name">Dr. Mara L. Valporte</div><div class="brand-role">Clinical Psychologist</div></div>
  <nav class="main-nav abs"><a>Home</a><a>Sessions</a><a>Resources</a><a>Bio</a><a>Contact</a></nav>
</header>

<div class="hero-shadow abs"></div>
<div class="hero abs" role="img" aria-label="Close-up photograph of a bright green leaf on a soft green background"></div>
<h1 class="hero-title abs">What is more<br>important<br>than your life?</h1>
<p class="hero-sub abs">- if you have any issues in your life, and need help from a professional phychologist with the proper education and experience contact me.</p>
<div class="slider-dots abs"><span></span><span></span><span class="active"></span><span></span></div>

<div class="rule abs" style="left:25px;top:749px;width:1152px"></div>

<section class="copy abs" style="left:32px;top:760px;width:572px">
  <h2 class="section-title" style="margin-bottom:10px">Getting help</h2>
  <p>I'm so glad you are here.&nbsp; Choosing to see a professional for issues in your life can be difficult but also possibly life changing. Many postpone seeking help because they believe doing so acknowledges failure on their part. Reallly? We seek the help of experts all the time (contractors, mechanics, chefs, etc...) and what is more important than your life? Consulting with a neutral party to act in your best&nbsp; interest can be time well spent.</p>
</section>

<div class="rule abs" style="left:25px;top:989px;width:582px"></div>

<section class="copy abs" style="left:32px;top:1013px;width:572px">
  <h2 class="section-title" style="margin-bottom:12px">Who to choose</h2>
  <p>If you are willing to take the time to invest in counseling, make sure that it is with someone that is worth your time.<br>Choose a licensed psychologist with a doctoral degree (Ph.D. or PsyD.) both have over 10 years of education in the field of psychology, extensive internships and comprehensive licensing exams. Others have far less education if any.</p>
  <p>Consider the therapist's approach to therapy.&nbsp; I use a straightforward approach (psychobabble available upon request) with brief, solution-oriented sessions.</p>
  <p>Experience also separates good psychologists from others with fewer and more proficient sessions. My&nbsp; 20+ years of professional experience and my life experience contributes to the empathetic perspective I use to relate to each person I see.&nbsp; I also believe it is the reason 90% of my practice is referral based and why many other psychologists in the area seek my services.</p>
  <p><strong style="font-weight:900">DO NOT COMPROMISE</strong>.&nbsp; Find an educated, licensed, experienced professional that you can relate to. Think about what it took to get you here and the importance resolving this issue can have on your life.</p>
</section>

<div class="portrait abs" role="img" aria-label="Portrait photograph of the psychologist"></div>

<h2 class="section-title side-title abs" style="left:798px;top:1190px">Education</h2>
<div class="side-list abs" style="left:798px;top:1240px">Doctoral Degree in Clinical Psychology<br>Masters Degree in Counseling Psychology<br>Doctoral Internship, Coastline Medical Center<br>Masters Internship, Bayside Clinic</div>

<div class="rule abs" style="left:798px;top:1354px;width:373px"></div>

<h2 class="section-title side-title abs" style="left:798px;top:1380px">Expertise</h2>
<div class="side-list abs" style="left:830px;top:1433px;width:308px">Dating, marriage, parenting, professional relationships, depression, anxiety issues, personality disorders, life management</div>

<div class="rule abs" style="left:25px;top:1607px;width:1152px"></div>

<div class="media-panel abs"></div>

<div class="media-card abs" style="left:144px">
  <div class="card-head">Video</div>
  <svg class="player abs" viewBox="0 0 298 262" role="img" aria-label="Embedded video player">
    <rect width="298" height="262" fill="#000"/>
    <rect x="129" y="103" width="40" height="40" rx="4" fill="#222"/>
    <path d="M142 113 L160 123 L142 133 Z" fill="#fff"/>
    <rect y="240" width="298" height="22" fill="#e6e6e6"/>
    <path d="M8 246 L16 251 L8 256 Z" fill="#555"/>
    <rect x="260" y="246" width="10" height="10" fill="none" stroke="#555" stroke-width="1.5"/>
  </svg>
  <div class="more abs"><span>See more videos</span><span class="btn">here</span></div>
</div>

<div class="media-card abs" style="left:727px">
  <div class="card-head">Radio Show</div>
  <div class="poster abs" role="img" aria-label="Poster for the Silver Harbor Tunes radio show with its hosts and Sunday air time"></div>
</div>

<footer class="site-footer abs"></footer>
<div class="foot-title abs" style="left:90px;top:2222px">Quick Links</div>
<div class="abs" style="left:82px;top:2258px;width:200px;height:1px;background:#444"></div>
<div class="foot-list abs" style="left:82px;top:2270px">- Home<br>- Sessions<br>- Resources<br>- Bio<br>- Contact</div>

<div class="foot-title abs" style="left:347px;top:2220px">Contact</div>
<div class="abs" style="left:340px;top:2256px;width:200px;height:1px;background:#444"></div>
<div class="foot-list abs" style="left:347px;top:2270px;line-height:19px">- 418 Linden Court, Suite 120<br>Harborview, CA 90412<br><span style="display:block;height:11px"></span>- (555) 214 3380<br><span style="display:block;height:11px"></span>- ml@drvalporte.com</div>

<div class="map abs" role="img" aria-label="Street map showing the office location"></div>

<div class="donate abs">A portion of all revenue is donated to</div>
<div class="badge-a abs"></div>
<div class="badge-b abs"></div>
<div class="badge-rating abs"></div>
<div class="share abs">Share on Chatterbook</div>

<div class="abs" style="left:80px;top:2455px;width:1040px;height:1px;background:#3a3a3a"></div>
<div class="copyright abs">© Copyright 2016 Dr. Valporte. All Rights Reserved.</div>

</body>
</html>
```